Multivitamin fruit drink in tetrapak

Label design for a 200 ml tetrapak which contains fruit juice with multivitamins in natural form . Product will be promoted to doctors and will follow a otx model. The target is children and women. Being a completely natural fortified multivitamin and mineral drink , the natural aspects to be highlighted. A white background is suggestive . Should not have more than 6 colors as this involves flexo printing.

Target Market(s)

Children and women through doctors recommendations

Industry/Entity Type

Pharmaceutical

Font styles to use
Serif
Sans Serif
Decorative

Requirements
Must have
• Pictures of fruit . Variant 1 is mango and variant 2 is orange. Brand name is Verosta. Can also suggest new names.
Nice to have
• The brand standing out, with white or softer color background
Should not have
• Should not have Dark background. Not funky or too colorful.

```html
<!DOCTYPE html>
<html lang="en">
<head>
<meta charset="utf-8">
<title>Verosta Multivitamins – Mango 200ml</title>
<link rel="stylesheet" href="https://fonts.googleapis.com/css2?family=Alfa+Slab+One&family=Open+Sans:wght@400;600&display=swap">
<style>
  :root {
    --page: #ececec;
    --white: #ffffff;
    --sun: #ffd200;
    --gold: #f5b400;
    --brand: #f2b600;
    --leaf: #8cc65a;
    --leaf-soft: #e3f1d2;
    --mango: #f3bf2a;
  }
  html, body {
    margin: 0;
    padding: 0;
    width: 1200px;
    height: 3070px;
    overflow: hidden;
    background: var(--page);
  }
  .canvas {
    position: relative;
    width: 1200px;
    height: 3070px;
  }
  .label {
    position: absolute;
    left: 105px;
    top: 460px;
    width: 993px;
    height: 2246px;
    overflow: hidden;
    background: linear-gradient(to bottom,
      var(--white) 0%,
      var(--white) 70%,
      #fff1b0 76%,
      var(--sun) 84%,
      var(--sun) 100%);
  }
  .leaf-artwork {
    position: absolute;
    left: 215px;
    top: 0;
    width: 778px;
    height: 972px;
    background: linear-gradient(to bottom left, var(--leaf) 0%, var(--leaf-soft) 55%, var(--white) 100%);
  }
  .side-band {
    position: absolute;
    left: 0;
    top: 0;
    width: 215px;
    height: 1120px;
    background: var(--sun);
  }
  .side-band__letters {
    position: absolute;
    left: 0;
    top: 240px;
    width: 215px;
    margin: 0;
    padding: 0;
    list-style: none;
    font-family: "Open Sans", sans-serif;
    font-size: 50px;
    line-height: 66px;
    color: var(--white);
    text-align: center;
  }
  .brand-name {
    position: absolute;
    left: 36px;
    top: 78px;
    width: 920px;
    margin: 0;
    font-family: "Alfa Slab One", serif;
    font-weight: 400;
    font-size: 150px;
    line-height: 1;
    letter-spacing: 6px;
    color: var(--brand);
    white-space: nowrap;
  }
  .tagline {
    position: absolute;
    left: 0;
    top: 1133px;
    width: 966px;
    margin: 0;
    font-family: "Open Sans", sans-serif;
    font-weight: 600;
    font-size: 54px;
    line-height: 72px;
    color: var(--gold);
    text-align: center;
  }
  .fruit-artwork {
    position: absolute;
    left: 151px;
    top: 1407px;
    width: 634px;
    height: 371px;
    background: var(--mango);
  }
  .flavour {
    position: absolute;
    left: 0;
    top: 1895px;
    width: 966px;
    margin: 0;
    font-family: "Open Sans", sans-serif;
    font-size: 70px;
    line-height: 100px;
    color: var(--white);
    text-align: center;
  }
  .volume {
    position: absolute;
    right: 50px;
    top: 2132px;
    margin: 0;
    font-family: "Open Sans", sans-serif;
    font-size: 52px;
    line-height: 72px;
    color: var(--white);
  }
</style>
</head>
<body>
<div class="canvas">
  <section class="label">
    <div class="leaf-artwork" role="img" aria-label="Watercolour splash of green leaves with small falling leaves"></div>

    <div class="side-band">
      <ul class="side-band__letters" aria-label="Multivitamins">
        <li>M</li><li>u</li><li>l</li><li>t</li><li>i</li><li>v</li><li>i</li><li>t</li><li>a</li><li>m</li><li>i</li><li>n</li><li>s</li>
      </ul>
    </div>

    <h1 class="brand-name">VEROSTA</h1>

    <p class="tagline">completely natural fortified<br>multivitamin and<br>mineral drink</p>

    <div class="fruit-artwork" role="img" aria-label="Photo of a ripe yellow mango"></div>

    <p class="flavour">MANGO</p>
    <p class="volume">200ml</p>
  </section>
</div>
</body>
</html>
```